Template for Vantor Advisory PowerPoint

We would like to create a new template for PowerPoint based on our current logo and graphic design guidelines. The template should reflect our corporate identity and be easy to use to create different kind of PowerPoint presentations for different kind of customers. The current design guideline that are attached reflect the "old" look of the PPT design and is only to be seen as a reference.
Vantor Advisory is a Management consulting company working within both public and private sector. We focus on strategic business development and work in close cooperation with the customer to make sure it is the customer that will become the hero, our work is to support and guide them to the top.
The design should reflect a modern company working in close cooperation with our customers to help them innovate and describe their future business model, and also help them to reach that goal!
Words and taglines that we use. Passion for the future. The power of the organisation. Power of thoughts. Inspiration. Engagement.
What we have in mind is a modern, clean and elegant design based on our current logo. Vantor Advisory is a Swedish Company working primarily on the Swedish market so the template must be possible to translate to Swedish (however the design can be done in english and be translated later)

Project Deadline Extended
Reason: I would like to extend the deadline to receive some more alternatives!

Project Deadline Extended
Reason: I'm out travelling and would like to extend the timeline to be able to choose the right design for our template. /Henrik

Target Market(s)

Our target market is within both private and public sector. Our main focus is CxO level executives within our clients organisation.

Industry/Entity Type

Management Consulting

Font styles to use
Sans Serif

Colors

Designer to choose colors to be used in the design.

Requirements
Must have
• A PPT template that contains both slides for traditional text and graphic. We like to work a lot with graphical presentations and try to limit the text on our slides to a minimum.
Nice to have
• Slides for different chapters within the presentation. Slides for powerful one-liners. Title slides. Thank you slides at the end.
Should not have
• Massive text....

```html
<!DOCTYPE html>
<html lang="en">
<head>
<meta charset="UTF-8">
<title>Vantor Advisory – Slide Divider Layout</title>
<link rel="stylesheet" href="https://fonts.googleapis.com/css2?family=Lato:wght@300;400;700;900&display=swap">
<style>
  :root {
    --crimson: #d31b4b;
    --crimson-deep: #c4123f;
    --crimson-light: #db3a63;
    --white: #ffffff;
    --rule: #bdbdbd;
    --ink: #333333;
  }
  * { margin: 0; padding: 0; box-sizing: border-box; }
  html, body { width: 1200px; height: 714px; overflow: hidden; background: var(--white); }
  .slide {
    position: relative;
    width: 1200px;
    height: 714px;
    font-family: "Lato", Arial, sans-serif;
    overflow: hidden;
  }
  .hero {
    position: absolute;
    left: 0; top: 0;
    width: 1200px; height: 658px;
    background: linear-gradient(135deg, var(--crimson) 0%, var(--crimson-deep) 100%);
  }
  .hero-shapes { position: absolute; left: 0; top: 0; }
  .section-number {
    position: absolute;
    right: -8px; top: 14px;
    width: 72px; height: 72px;
    border-radius: 50%;
    background: var(--crimson-deep);
    color: var(--white);
    font-size: 19px;
    font-weight: 400;
    display: flex; align-items: center;
    padding-left: 16px;
  }
  .divider-title {
    position: absolute;
    left: 57px; top: 300px;
    color: var(--white);
    font-size: 45px;
    line-height: 1;
    font-weight: 300;
    letter-spacing: 0.2px;
  }
  .divider-title strong { font-weight: 900; }
  .divider-subtitle {
    position: absolute;
    left: 58px; top: 366px;
    color: var(--white);
    font-size: 24px;
    font-weight: 400;
  }
  .footer {
    position: absolute;
    left: 0; top: 658px;
    width: 1200px; height: 56px;
    border-top: 1px solid var(--rule);
    background: var(--white);
  }
  .progress-dots {
    position: absolute;
    left: 18px; top: 21px;
    display: flex; gap: 5px;
  }
  .progress-dots span {
    width: 14px; height: 14px;
    border-radius: 50%;
    background: var(--crimson);
  }
  .brand {
    position: absolute;
    right: 20px; top: 11px;
    display: flex; align-items: center; gap: 8px;
    color: var(--ink);
    font-size: 27px;
    font-weight: 300;
  }
  .brand-dot {
    width: 20px; height: 20px;
    border-radius: 50%;
    background: var(--crimson);
  }
</style>
</head>
<body>
<div class="slide">
  <div class="hero" role="img" aria-label="Top-down photo of a team working at a desk with laptop and printed charts, tinted crimson">
    <svg class="hero-shapes" width="1200" height="658" viewBox="0 0 1200 658" aria-hidden="true">
      <circle cx="940" cy="369" r="226" fill="var(--crimson-light)" opacity="0.35"/>
      <circle cx="1160" cy="345" r="205" fill="var(--crimson-light)" opacity="0.3"/>
    </svg>
  </div>

  <div class="section-number">01</div>

  <h1 class="divider-title"><strong>SLIDE DIVIDER</strong> LAYOUT</h1>
  <p class="divider-subtitle">Your Subtitle Here</p>

  <footer class="footer">
    <div class="progress-dots"><span></span><span></span><span></span><span></span><span></span></div>
    <div class="brand">Vantor Advisory<span class="brand-dot"></span></div>
  </footer>
</div>
</body>
</html>
```